IV Bag Graphic for IV Therapy Bar

Hello we are offering an IV Therapy Bar to our medical practice. We already have a logo would like a cool design label for the IV bag. We will utilize this label for social media advertising, a sticker for the saline bag and marketing material. Woukd like something unique, sharp, bold and professional. We signed up for the Social Media package so the design will need to hold and be creative.

Target Market(s)

25-35 yrs old

Requirements
Must have
• Bellwood Clinical Research name and logo- Clear inference it is IV therapy
Nice to have
• Innovation- Lines to write Name - Also please give examples of the different IV therapies (Myers cocktail) etc (screenshot example of therapies is attached)
Should not have
• In the attached examples the packaging and label are black, in open.

```html
<!DOCTYPE html>
<html lang="en">
<head>
<meta charset="utf-8">
<title>Myers Cocktail Wellness Drip Label</title>
<link href="https://fonts.googleapis.com/css2?family=Montserrat:wght@400;500;700&family=Roboto+Condensed:wght@500;700&display=swap" rel="stylesheet">
<style>
  :root {
    --stage: #6b6b6b;
    --navy: #0b3a9c;
    --royal: #0a4fb8;
    --cyan: #00c8f5;
    --sky-top: #e6f8fd;
    --sky-bottom: #cdf2fc;
    --paper: #ffffff;
    --form-grey: #6a6a6a;
    --rule-grey: #a8a8a8;
  }
  * { margin: 0; padding: 0; box-sizing: border-box; }
  html, body {
    width: 912px; height: 1200px; overflow: hidden;
    background: var(--stage);
  }
  .label {
    position: absolute; left: 137px; top: 95px;
    width: 637px; height: 962px; overflow: hidden;
    background: var(--paper);
    font-family: "Montserrat", sans-serif;
  }
  .label__sky {
    position: absolute; inset: 0 0 auto 0; height: 700px;
    background: linear-gradient(180deg, var(--sky-top) 0%, var(--sky-bottom) 100%);
  }
  .label__texture {
    position: absolute; inset: 0;
    background: radial-gradient(ellipse at 75% 20%, rgba(255,255,255,0.55), rgba(255,255,255,0) 60%);
  }
  .label__art { position: absolute; inset: 0; }
  .title {
    position: absolute; left: 67px; top: 55px;
    color: var(--navy); font-weight: 700;
    font-size: 58px; line-height: 57px; letter-spacing: -0.5px;
  }
  .subtitle {
    position: absolute; left: 69px; top: 182px; width: 317px; height: 46px;
    background: linear-gradient(90deg, var(--navy) 0%, var(--royal) 35%, var(--cyan) 55%, var(--royal) 75%, var(--navy) 100%);
    color: #fff; font-weight: 500; font-size: 31px; line-height: 46px;
    text-align: center; letter-spacing: 0.5px;
  }
  .ingredients {
    position: absolute; left: 69px; top: 261px; list-style: none;
    color: var(--navy); font-size: 29px; font-weight: 400; line-height: 39px;
  }
  .ingredients li::before { content: "+ "; }
  .badge {
    position: absolute; top: 489px; width: 86px; height: 86px;
    border-radius: 50%; border: 1.5px dotted var(--navy);
    display: flex; align-items: center; justify-content: center;
  }
  .badge__inner {
    width: 76px; height: 76px; border-radius: 50%;
    border: 1.5px solid var(--navy);
    display: flex; flex-direction: column; align-items: center; justify-content: center;
    font-family: "Roboto Condensed", sans-serif; color: var(--navy);
    text-align: center; padding-top: 12px;
  }
  .badge--natural { left: 66px; }
  .badge--quality { left: 178px; }
  .badge__big { font-weight: 700; font-size: 14px; line-height: 13px; }
  .badge__small { font-weight: 500; font-size: 10px; line-height: 12px; }
  .volume {
    position: absolute; left: 232px; top: 670px; width: 58px; height: 58px;
    border-radius: 50%;
    background: linear-gradient(160deg, var(--royal), var(--cyan) 55%, var(--royal));
    color: #fff; font-size: 14px; line-height: 58px; text-align: center;
  }
  .brand {
    position: absolute; left: 420px; top: 680px; width: 194px;
    text-align: center; color: var(--royal); font-weight: 700;
  }
  .brand__name { font-size: 25px; line-height: 26px; letter-spacing: 0.5px; }
  .brand__tag { font-size: 12.5px; line-height: 16px; letter-spacing: 0.3px; }
  .patient-form {
    position: absolute; left: 50px; top: 828px; width: 557px;
    color: var(--form-grey); font-size: 17px;
  }
  .patient-form__row {
    display: flex; align-items: flex-end; height: 36.5px;
  }
  .patient-form__line {
    flex: 1; margin-left: 6px; margin-bottom: 6px;
    border-bottom: 1px dotted var(--rule-grey);
  }
</style>
</head>
<body>
<main class="label">
  <div class="label__sky"></div>
  <div class="label__texture" role="img" aria-label="Faint hexagonal molecule pattern across the light blue upper area"></div>

  <svg class="label__art" width="637" height="962" viewBox="0 0 637 962" aria-hidden="true">
    <defs>
      <linearGradient id="ribbon-upper" x1="0" y1="0" x2="1" y2="0">
        <stop offset="0" stop-color="#0b3a9c"/>
        <stop offset="0.45" stop-color="#00c8f5"/>
        <stop offset="0.75" stop-color="#0e8ad8"/>
        <stop offset="1" stop-color="#0b3a9c"/>
      </linearGradient>
      <linearGradient id="ribbon-lower" x1="0" y1="0" x2="1" y2="0.4">
        <stop offset="0" stop-color="#00c8f5"/>
        <stop offset="0.5" stop-color="#0a8bd6"/>
        <stop offset="1" stop-color="#0b3a9c"/>
      </linearGradient>
    </defs>
    <!-- white field beneath the wave -->
    <path d="M0,684 C160,676 320,585 430,530 C520,490 590,498 637,520 L637,962 L0,962 Z" fill="#ffffff"/>
    <!-- sky wedge between crossing ribbons -->
    <path d="M275,636 C340,600 390,570 430,545 C360,590 320,610 300,625 Z" fill="#cdf2fc"/>
    <!-- lower ribbon -->
    <path d="M300,618 C370,710 470,810 637,815 L637,827 C470,830 380,760 268,640 Z" fill="url(#ribbon-lower)"/>
    <!-- upper ribbon -->
    <path d="M0,676 C160,668 320,570 430,515 C520,472 590,476 637,513 L637,521 C570,496 510,505 410,566 C300,632 160,694 0,690 Z" fill="url(#ribbon-upper)"/>

    <!-- bracket line -->
    <polyline points="273,65 567,65 567,328" fill="none" stroke="#0b3a9c" stroke-width="2"/>

    <!-- heart in hand icon -->
    <g fill="none" stroke="#0b3a9c" stroke-width="2.2" stroke-linejoin="round" stroke-linecap="round">
      <path d="M567,400 C540,380 535,368 535,358 C535,346 545,340 553,340 C560,340 565,345 567,350 C569,345 574,340 581,340 C589,340 599,346 599,358 C599,368 594,380 567,400 Z"/>
      <polyline points="546,371 556,371 561,361 567,381 572,367 576,371 588,371"/>
      <path d="M521,418 L545,412 C555,410 570,412 580,414 C586,415 586,424 580,425 L556,426"/>
      <path d="M555,427 L584,427 L605,416 C611,412 608,404 601,407 L584,414"/>
      <path d="M521,418 C528,432 540,446 560,446 L584,440"/>
      <rect x="503" y="415" width="14" height="32" rx="2" transform="rotate(-38 510 431)"/>
    </g>

    <!-- badge glyphs -->
    <g fill="none" stroke="#0b3a9c" stroke-width="1.4">
      <path d="M109,500 C103,505 103,512 109,517 C115,512 115,505 109,500 Z"/>
      <ellipse cx="109" cy="519" rx="9" ry="3"/>
    </g>
    <g fill="#0b3a9c">
      <circle cx="221" cy="512" r="7"/>
      <circle cx="216" cy="503" r="2.5"/>
    </g>
  </svg>

  <h1 class="title">MYERS<br>COCKTAIL</h1>
  <div class="subtitle">WELLNESS DRIP</div>

  <ul class="ingredients">
    <li>B - COMPLEX VITAMINS</li>
    <li>VITAMIN B12</li>
    <li>MAGNEISUM</li>
    <li>VITAMIN C</li>
    <li>CALCIUM</li>
  </ul>

  <div class="badge badge--natural">
    <div class="badge__inner">
      <span class="badge__big">NATURAL</span>
      <span class="badge__big">THERAPY</span>
    </div>
  </div>
  <div class="badge badge--quality">
    <div class="badge__inner">
      <span class="badge__big">QUALITY</span>
      <span class="badge__small">INGREDIENT</span>
    </div>
  </div>

  <div class="volume">100ml.</div>

  <div class="brand">
    <div class="brand__name">BELLWOOD</div>
    <div class="brand__tag">CLINICAL RESEARCH</div>
  </div>

  <div class="patient-form">
    <div class="patient-form__row"><span>PATIENT NAME :</span><span class="patient-form__line"></span></div>
    <div class="patient-form__row"><span>PATIENT #</span><span class="patient-form__line"></span></div>
    <div class="patient-form__row"><span>START TIME :</span><span class="patient-form__line"></span></div>
  </div>
</main>
</body>
</html>
```